New Plumbing Company

We are looking for a smart and creative business card design for our new plumbing company. We are looking for creativity and originality in our business cards.

Industry/Entity Type

Plumbing

Contact Information for Business Card

Crestline Plumbing
Peter Halvane
Managing Director
Telephone Number : 0481529604
Email : service@crestlineplumbing.com.au
Website : www.crestlineplumbing.com.au
Lic. 508264K

Colors
0692cd
33a6d7
000000

Requirements
Must have
• I want the business card to be designed on a black background using the blue tones i have selected as seen in the company logo.

```html
<!DOCTYPE html>
<html lang="en">
<head>
<meta charset="utf-8">
<title>Crestline Plumbing – Business Card</title>
<link rel="stylesheet" href="https://fonts.googleapis.com/css2?family=Lato:wght@400;700&display=swap">
<style>
  :root {
    --page-bg: #ececec;
    --card-edge: #f7f7f7;
    --card-black: #1d1d1d;
    --brand-blue: #0692cd;
    --band-blue: #1b7bc0;
    --band-fold: #0d4f80;
    --light-blue: #33a6d7;
    --text-white: #ffffff;
    --text-soft: #dfeaf3;
  }
  * { box-sizing: border-box; margin: 0; padding: 0; }
  html, body {
    width: 1200px; height: 801px; overflow: hidden;
    background: var(--page-bg);
    font-family: "Lato", sans-serif;
  }
  .business-card {
    position: absolute;
    left: 405px; top: 80px;
    width: 390px; height: 640px;
    background: var(--card-edge);
    box-shadow: 0 6px 18px rgba(0,0,0,0.12);
  }
  .card-body {
    position: absolute;
    left: 30px; right: 30px; top: 0; bottom: 0;
    background: var(--card-black);
  }
  .brand {
    position: absolute;
    top: 170px; left: 0; right: 0;
    display: flex; align-items: center; justify-content: center; gap: 12px;
  }
  .brand-dot {
    width: 34px; height: 34px; border-radius: 50%;
    border: 3px solid var(--brand-blue);
  }
  .brand-name {
    font-size: 30px; font-weight: 400;
    color: var(--text-white);
    letter-spacing: 0.5px;
  }
  .name-band {
    position: absolute;
    top: 305px; left: -6px; width: 402px; height: 72px;
    background: var(--band-blue);
    display: flex; align-items: center;
    padding-left: 40px; gap: 14px;
  }
  .band-fold {
    position: absolute; top: 377px;
  }
  .band-fold.left { left: -6px; }
  .band-fold.right { right: -6px; }
  .avatar-circle {
    width: 50px; height: 50px; border-radius: 50%;
    background: var(--text-white);
    display: flex; align-items: center; justify-content: center;
  }
  .holder-name {
    font-size: 24px; font-weight: 700; color: var(--text-white);
    letter-spacing: 0.5px; line-height: 1.05;
  }
  .holder-role, .holder-licence {
    font-size: 14px; font-weight: 400; color: var(--text-soft);
    line-height: 1.15;
  }
  .contact-list {
    position: absolute;
    top: 430px; left: 0; right: 0;
    list-style: none;
    padding-left: 16px;
  }
  .contact-item {
    display: flex; align-items: center; gap: 12px;
    height: 30px; margin-bottom: 38px;
    font-size: 15px; color: var(--text-white);
  }
  .contact-icon {
    width: 28px; height: 28px; flex: none;
    background: var(--brand-blue);
    display: flex; align-items: center; justify-content: center;
    box-shadow: 2px 2px 0 #0a5d86;
  }
</style>
</head>
<body>
  <article class="business-card">
    <div class="card-body">
      <header class="brand">
        <span class="brand-dot"></span>
        <span class="brand-name">Crestline Plumbing</span>
      </header>
    </div>

    <svg class="band-fold left" width="14" height="12" viewBox="0 0 14 12"><polygon points="0,0 14,0 14,12" fill="var(--band-fold)"/></svg>
    <svg class="band-fold right" width="14" height="12" viewBox="0 0 14 12"><polygon points="0,0 14,0 0,12" fill="var(--band-fold)"/></svg>

    <section class="name-band">
      <div class="avatar-circle" role="img" aria-label="Contact person icon">
        <svg width="26" height="26" viewBox="0 0 26 26"><circle cx="13" cy="13" r="11" fill="var(--band-blue)"/></svg>
      </div>
      <div class="holder">
        <div class="holder-name">PETER HALVANE</div>
        <div class="holder-role">Managing Director</div>
        <div class="holder-licence">Lic. 508264K</div>
      </div>
    </section>

    <ul class="contact-list">
      <li class="contact-item">
        <span class="contact-icon">
          <svg width="18" height="18" viewBox="0 0 18 18" fill="none" stroke="#fff" stroke-width="1.5">
            <circle cx="9" cy="9" r="7.5"/><ellipse cx="9" cy="9" rx="3.2" ry="7.5"/><line x1="1.5" y1="9" x2="16.5" y2="9"/>
          </svg>
        </span>
        <span class="contact-text">www.crestlineplumbing.com.au</span>
      </li>
      <li class="contact-item">
        <span class="contact-icon">
          <svg width="18" height="18" viewBox="0 0 18 18">
            <circle cx="9" cy="9" r="8" fill="none" stroke="#fff" stroke-width="1.4"/>
            <path d="M6 4.5 L7.6 4.5 L8.2 7 L7.2 7.8 C7.8 9.2 8.8 10.2 10.2 10.8 L11 9.8 L13.5 10.4 L13.5 12 C9 12.5 5.5 9 6 4.5 Z" fill="#fff"/>
          </svg>
        </span>
        <span class="contact-text">0481529604</span>
      </li>
      <li class="contact-item">
        <span class="contact-icon">
          <svg width="18" height="14" viewBox="0 0 18 14">
            <rect x="1" y="1" width="16" height="12" fill="#fff"/>
            <polyline points="1,1 9,8 17,1" fill="none" stroke="var(--brand-blue)" stroke-width="1.4"/>
          </svg>
        </span>
        <span class="contact-text">service@crestlineplumbing.com.au</span>
      </li>
    </ul>
  </article>
</body>
</html>
```